Build a new Capability Statement for a labour support and maintenance company

Hi Everyone,
We wish to update our capability statement. Attached is a powerpoint that has the key ideas with random pictures we would like in the document. I have also attached a competitors document as a sample of the things we like. This document is being sent to our entire client base which includes Tier 1 mining companies like Vela Corran & KQS

Target Market(s)

Mining Companies

Industry/Entity Type

Mining

Colors

Designer to choose colors to be used in the design.

```html
<!DOCTYPE html>
<html lang="en">
<head>
<meta charset="utf-8">
<title>TMR Capability Statement – Cover Spread</title>
<link rel="stylesheet" href="https://fonts.googleapis.com/css2?family=Montserrat:wght@400;600;700;800&display=swap">
<style>
  :root {
    --backdrop: #a9a9ad;
    --charcoal: #3a3a3c;
    --paper: #e4e4e6;
    --orange: #e8891c;
    --title-orange: #e0822a;
    --ink: #1f1f21;
    --white: #ffffff;
  }
  * { box-sizing: border-box; margin: 0; padding: 0; }
  html, body {
    width: 1200px; height: 900px; overflow: hidden;
    background: var(--backdrop);
    font-family: "Montserrat", sans-serif;
  }
  .spread {
    position: absolute; left: 200px; top: 167px;
    width: 800px; height: 566px;
    display: flex;
  }
  .page {
    position: relative; width: 400px; height: 566px;
    background: var(--paper); overflow: hidden;
  }

  /* Back cover */
  .back-cover .dark-field {
    position: absolute; left: 0; top: 0; width: 100%; height: 432px;
    background: var(--charcoal);
  }
  .accent-square {
    position: absolute; width: 59px; height: 87px;
    background: var(--orange);
  }
  .back-cover .accent-square { left: 44px; top: 387px; }
  .contact-block {
    position: absolute; left: 122px; top: 389px;
    color: var(--white); font-style: normal;
    font-size: 6px; line-height: 8px; font-weight: 400;
  }
  .contact-block strong { font-weight: 700; }
  .web-address {
    position: absolute; top: 481px;
    font-size: 6px; font-weight: 700; letter-spacing: 0.18em;
    color: var(--ink);
  }
  .back-cover .web-address { left: 44px; }

  /* Front cover */
  .front-cover .header-band {
    position: absolute; left: 0; top: 0; width: 117px; height: 140px;
    background: linear-gradient(90deg, #b9b9bc 0%, #f2f2f3 35%, #8f8f93 70%, #4a4a4d 100%);
  }
  .brand {
    position: absolute; right: 27px; top: 70px;
  }
  .brand-name {
    display: flex; align-items: center; gap: 8px;
    font-size: 34px; font-weight: 800; color: var(--ink); line-height: 1;
  }
  .brand-dot { width: 18px; height: 18px; border-radius: 50%; background: var(--orange); }
  .brand-tagline {
    margin-top: 3px; margin-left: 26px;
    font-size: 5.5px; font-weight: 800; color: var(--ink); letter-spacing: 0.04em;
  }
  .cover-photo {
    position: absolute; left: 0; top: 140px; width: 100%; height: 292px;
    background: linear-gradient(180deg,
      #6f8fa8 0%, #b8a99a 30%, #f0b06a 48%, #c5693a 60%, #9a4a2c 78%, #6e3422 100%);
  }
  .cover-title {
    position: absolute; right: 27px; top: 170px; text-align: right;
  }
  .cover-kicker {
    font-size: 10px; font-weight: 400; letter-spacing: 0.32em; color: #3f3f42;
  }
  .cover-heading {
    font-size: 21px; font-weight: 700; color: var(--title-orange); letter-spacing: 0.01em;
  }
  .front-cover .accent-square { left: 315px; top: 390px; }
  .front-cover .web-address { left: 315px; top: 484px; }
</style>
</head>
<body>
  <main class="spread">
    <section class="page back-cover">
      <div class="dark-field"></div>
      <div class="accent-square"></div>
      <address class="contact-block">
        <strong>Harlow Industries, Inc.</strong><br>
        Brookfield, NY 11820 | Harlow West, Inc.<br>
        Redmesa, NV 89560 | 800.555.0142<br>
        www.harlowgroup.net
      </address>
      <p class="web-address">WWW.TMR.COM</p>
    </section>

    <section class="page front-cover">
      <div class="header-band"></div>
      <div class="brand">
        <div class="brand-name"><span class="brand-dot"></span>TMR</div>
        <div class="brand-tagline">TIDEMARK MINING &amp; RELIABILITY</div>
      </div>
      <div class="cover-photo" role="img" aria-label="Large mining excavator and a white site utility vehicle on red earth at sunset"></div>
      <div class="cover-title">
        <p class="cover-kicker">COMPANY PROFILE</p>
        <h1 class="cover-heading">CAPABILITY STATEMENT</h1>
      </div>
      <div class="accent-square"></div>
      <p class="web-address">WWW.TMR.COM</p>
    </section>
  </main>
</body>
</html>
```